DRIVEMEND: Data Rescue from hard drives

Create new web site. Our existing site is at www.drivemend.com.au

The site must show that our main business is recovering data from crashed hard disks. Color theme is blue. Existing logo can be used.

I want to be able to change the images and text later.

Text could be like this:

For when you didn't make a backup...

Some information is like gold to your business. We can recover data from corrupted disks. This includes your documents, Mailbox contacts, financials, contracts, photos or records.

Drivemend has the recovery tools, software and skills. If you have a damaged disk or files we will make our best effort to recover these for you and put them on a new disk, the Cloud, a DVD or other media.

We strongly suggest that in the event of disk damage the less that you attempt to recover files yourself, the better are our chances of getting your files back. Just turn your computer off and get the disk or the whole computer to us.

Our charges are:

•Standard recovery: $450 including GST
(no recovery= no charge)

•Additional work (if required): by arrangement

•New Media: at cost

Recovery service at no charge for computers damaged in WA Bushfires. (Offer does not include supplying free new equipment)

Please see our "Testimonials" link above for remarks by happy customers. We have been in business for nineteen years and plan on staying that way, keeping you in business.

Small business

Business

Requirements
Must have
• Must suit new Google design rules to be mobile-device-friendly.

```html
<!DOCTYPE html>
<html lang="en">
<head>
<meta charset="utf-8">
<meta name="viewport" content="width=device-width, initial-scale=1">
<title>DRIVEMEND – Data Rescue from Hard Drives</title>
<link href="https://fonts.googleapis.com/css2?family=Raleway:wght@400;500;600&family=Open+Sans:wght@400&display=swap" rel="stylesheet">
<style>
  :root {
    --navy: #0e2438;
    --navy-mid: #163a5a;
    --brand: #1f4f86;
    --sky: #5b9bd5;
    --sky-light: #a4cbee;
    --text: #333;
    --muted: #666;
    --white: #fff;
  }
  * { box-sizing: border-box; margin: 0; padding: 0; }
  html, body { width: 1023px; height: 1200px; overflow: hidden; background: var(--white); }
  body { font-family: "Open Sans", sans-serif; color: var(--text); position: relative; }
  .wrap { width: 710px; margin-left: 156px; position: relative; }

  .site-header { height: 100px; position: relative; }
  .brand { position: absolute; left: 2px; top: 33px; display: flex; align-items: center; gap: 12px; }
  .brand-mark { width: 48px; height: 48px; border-radius: 50%; background: var(--brand); }
  .brand-name { font-family: "Raleway", sans-serif; font-weight: 500; font-size: 25px; color: var(--brand); }
  .enquiry { position: absolute; right: 2px; top: 44px; text-align: right; }
  .enquiry-label { font-family: "Raleway", sans-serif; font-size: 14px; color: var(--sky); }
  .enquiry-phone { font-family: "Raleway", sans-serif; font-weight: 500; font-size: 20px; color: var(--navy); display: flex; align-items: center; gap: 4px; margin-top: 1px; }

  .main-nav { height: 45px; background: linear-gradient(var(--navy-mid), var(--navy)); display: flex; }
  .main-nav a { font-family: "Raleway", sans-serif; font-size: 12px; color: var(--white); text-decoration: none; white-space: nowrap;
    display: flex; align-items: center; justify-content: center; border-right: 1px solid rgba(255,255,255,.12); }
  .main-nav a:last-child { border-right: none; }
  .nav-home { width: 70px; } .nav-cloud { width: 106px; } .nav-emergency { width: 137px; }
  .nav-repairs { width: 124px; } .nav-testimonials { width: 96px; } .nav-clients { width: 89px; } .nav-about { width: 88px; }

  .hero { height: 324px; position: relative; background: linear-gradient(120deg, #d9dbdd 0%, #b8bbbe 45%, #8f9397 70%, #c9cdd1 100%); }
  .hero-caption { position: absolute; left: 0; top: 121px; width: 287px; height: 96px; background: rgba(120,175,225,.82);
    clip-path: polygon(0 0, 100% 0, 92% 100%, 0 100%); padding: 22px 0 0 29px;
    font-family: "Raleway", sans-serif; font-weight: 500; font-size: 20px; line-height: 27px; color: var(--white); text-transform: uppercase; }
  .hero-dots { position: absolute; left: 323px; top: 304px; display: flex; gap: 4px; }
  .hero-dots span { width: 13px; height: 13px; border-radius: 50%; background: var(--white); }
  .hero-dots span:first-child { background: #111; }

  .intro { display: flex; justify-content: space-between; padding-top: 36px; height: 250px; }
  .intro-text { width: 416px; }
  .intro h1 { font-family: "Raleway", sans-serif; font-weight: 400; font-size: 20px; color: var(--navy); margin-bottom: 11px; }
  .intro p { font-size: 8.6px; line-height: 14.5px; color: var(--text); margin-bottom: 7px; }
  .charges { width: 254px; }
  .charges h2 { font-family: "Raleway", sans-serif; font-weight: 400; font-size: 19px; color: var(--brand); margin-bottom: 10px; }
  .charges li { list-style: none; display: flex; gap: 9px; font-family: "Raleway", sans-serif; font-size: 11px; line-height: 14.5px; color: var(--navy-mid); margin-bottom: 15px; }
  .charges svg { flex: none; margin-top: 1px; }

  .offer { position: absolute; left: 0; top: 695px; width: 1023px; height: 235px; border-top: 1px solid #ddd; }
  .offer-photo { position: absolute; left: 455px; top: 0; width: 545px; height: 235px;
    background: radial-gradient(ellipse at 55% 60%, #8c8f93 0%, #c2c4c7 45%, #eef0f2 80%, #fff 100%); }
  .offer-text { position: absolute; left: 157px; top: 55px; width: 340px; }
  .offer h2 { font-family: "Raleway", sans-serif; font-weight: 500; font-size: 14.5px; line-height: 22px; color: #222; }
  .offer .note { font-size: 11px; color: #444; margin: 4px 0 11px; }
  .offer .small { width: 330px; font-size: 7.8px; line-height: 13.5px; color: var(--muted); }

  .testimonials-band { position: absolute; left: 0; top: 930px; width: 1023px; height: 168px; text-align: center;
    background: linear-gradient(var(--sky-light), var(--sky)); color: var(--white); padding-top: 42px; font-family: "Raleway", sans-serif; }
  .testimonials-band h2 { font-weight: 400; font-size: 18.5px; }
  .testimonials-band p { font-size: 12.5px; margin-top: 4px; }
  .btn { display: inline-block; margin-top: 20px; background: var(--navy); color: var(--white); font-size: 11.5px;
    padding: 10px 19px; text-decoration: none; border-radius: 2px; }

  .site-footer { position: absolute; left: 0; top: 1098px; width: 1023px; height: 102px; background: linear-gradient(var(--navy-mid), var(--navy)); }
  .footer-nav { position: absolute; left: 162px; top: 33px; font-family: "Raleway", sans-serif; font-size: 11.5px; color: var(--white); white-space: nowrap; }
  .footer-nav a { color: var(--white); text-decoration: none; }
  .footer-nav .sep { margin: 0 5px; }
  .legal { position: absolute; left: 162px; top: 57px; font-size: 8.5px; color: #4e6e8c; }
  .social { position: absolute; left: 796px; top: 31px; display: flex; gap: 9px; }
  .social span { width: 18px; height: 18px; border-radius: 50%; background: var(--white); }
</style>
</head>
<body>
  <div class="wrap">
    <header class="site-header">
      <div class="brand"><span class="brand-mark"></span><span class="brand-name">DRIVEMEND</span></div>
      <div class="enquiry">
        <div class="enquiry-label">Enquiry Now</div>
        <div class="enquiry-phone">
          <svg width="20" height="20" viewBox="0 0 20 20"><circle cx="10" cy="10" r="9" fill="none" stroke="#5b9bd5" stroke-width="1.5"/><circle cx="10" cy="10" r="6.5" fill="#5b9bd5"/><path d="M7.5 6.5c.6 2.8 2.4 4.7 5 5.6l1-1.2-1.6-.9-.8.7c-1-.6-1.7-1.4-2.2-2.4l.7-.8-.8-1.6z" fill="#fff"/></svg>
          08 9400 2718
        </div>
      </div>
    </header>

    <nav class="main-nav">
      <a class="nav-home" href="#">Home</a><a class="nav-cloud" href="#">Cloud Services</a><a class="nav-emergency" href="#">Emergency Services</a><a class="nav-repairs" href="#">Computer Repairs</a><a class="nav-testimonials" href="#">Testimonials</a><a class="nav-clients" href="#">Our Clients</a><a class="nav-about" href="#">About Us</a>
    </nav>

    <section class="hero" role="img" aria-label="Technician in gloves repairing an opened hard drive on a lab bench">
      <div class="hero-caption">For when you didn't<br>make a backup</div>
      <div class="hero-dots"><span></span><span></span><span></span><span></span></div>
    </section>

    <section class="intro">
      <div class="intro-text">
        <h1>Welcome to Our Website Mainpage</h1>
        <p>Some information is like gold to your business. We can recover data from corrupted disks. This includes your documents, Mailbox contacts, financials, contracts, photos or records. Drivemend has the recovery tools, software and skills. If you have a damaged disk or fileswe will make our best effort to recover these for you and put them on a new disk, the Cloud, a DVD or other media.</p>
        <p>We strongly suggest that in the event of disk damage the less that you attempt to recoverfiles yourself, the better are our chances of getting your files back. Just turn yourcomputer off and get the disk or the whole computer to us.</p>
      </div>
      <div class="charges">
        <h2>Our charges are:</h2>
        <ul>
          <li><svg width="16" height="16" viewBox="0 0 16 16"><circle cx="8" cy="8" r="8" fill="#163a5a"/><path d="M4.5 8.2l2.4 2.3 4.6-4.8" fill="none" stroke="#fff" stroke-width="1.8"/></svg>Standard recovery: $450 including GST (no recovery= no charge)</li>
          <li><svg width="16" height="16" viewBox="0 0 16 16"><circle cx="8" cy="8" r="8" fill="#163a5a"/><path d="M4.5 8.2l2.4 2.3 4.6-4.8" fill="none" stroke="#fff" stroke-width="1.8"/></svg>Additional work (if required): by arrangement</li>
          <li><svg width="16" height="16" viewBox="0 0 16 16"><circle cx="8" cy="8" r="8" fill="#163a5a"/><path d="M4.5 8.2l2.4 2.3 4.6-4.8" fill="none" stroke="#fff" stroke-width="1.8"/></svg>New Media: at cost</li>
        </ul>
      </div>
    </section>
  </div>

  <section class="offer">
    <div class="offer-photo" role="img" aria-label="Hands holding an opened hard drive with a screwdriver"></div>
    <div class="offer-text">
      <h2>Recovery service at no charge for computers damaged in WA Bushfires.</h2>
      <p class="note">(Offer does not include supplying free new equipment)</p>
      <p class="small">In massa libero interdum nec interdum vel blandit sed nulla In ullamcorper est eget tempor cursus neque mi consectetuer mi a ultricies massa est sed nisl Class aptent taciti sociosqu ad litora torquent per conubia nostra per inceptos</p>
    </div>
  </section>

  <section class="testimonials-band">
    <h2>Please see our "Testimonials" link above for remarks by happy customers.</h2>
    <p>We have beenin business for nineteen years and plan on staying that way, keeping you in business.</p>
    <a class="btn" href="#">View Testimonials</a>
  </section>

  <footer class="site-footer">
    <div class="footer-nav">
      <a href="#">Home</a><span class="sep">|</span><a href="#">Cloud Services</a><span class="sep">|</span><a href="#">Emergency Services</a><span class="sep">|</span><a href="#">Computer Repairs</a><span class="sep">|</span><a href="#">Testimonials</a><span class="sep">|</span><a href="#">Our Clients</a><span class="sep">|</span><a href="#">About Us</a>
    </div>
    <div class="legal">© 2015 Company Name &nbsp;All right reserved &nbsp;Term of Use</div>
    <div class="social" aria-label="Social links"><span></span><span></span><span></span></div>
  </footer>
</body>
</html>
```